" Venda de planos de assistência familiar oferecendo uma rede descontos e funerais para os seus associados ; Serviços funerários; Venda de coroa de flores e arranjos. "

```html
<!DOCTYPE html>
<html lang="pt-BR">
<head>
<meta charset="utf-8">
<title>Laço Sereno — Cartão de visita</title>
<link rel="stylesheet" href="https://fonts.googleapis.com/css2?family=Montserrat:wght@400;600;800&display=swap">
<style>
  :root {
    --teal: #1e8c82;
    --teal-deep: #17756d;
    --aqua: #5cc9c0;
    --white: #ffffff;
    --ink: #4a4f52;
    --ghost: #e9ecec;
    --bg: #eef0ef;
  }
  * { box-sizing: border-box; margin: 0; padding: 0; }
  html, body { width: 1200px; height: 1200px; overflow: hidden; }
  body {
    background: var(--bg);
    font-family: "Montserrat", Arial, sans-serif;
    display: flex; flex-direction: column; align-items: center; justify-content: center;
    gap: 60px;
  }
  .card {
    position: relative; width: 900px; height: 514px; overflow: hidden;
    box-shadow: 0 10px 30px rgba(0,0,0,.12);
  }
  .card--front { background: var(--teal); }
  .card--back { background: var(--white); }

  .pattern--front {
    position: absolute; top: -20px; right: -20px; width: 420px; height: 300px;
    border-bottom-left-radius: 220px;
    background: radial-gradient(circle at 70% 30%, rgba(92,201,192,.55), rgba(255,255,255,.08) 70%, transparent);
  }
  .pattern--back {
    position: absolute; left: 0; top: 0; width: 440px; height: 400px;
    border-bottom-right-radius: 260px;
    background: radial-gradient(circle at 40% 40%, var(--ghost), rgba(233,236,236,0) 75%);
  }

  .brand { position: absolute; display: flex; flex-direction: column; }
  .brand__row { display: flex; align-items: center; gap: 12px; }
  .brand__dot { width: 22px; height: 22px; border-radius: 50%; }
  .brand__name { font-weight: 800; letter-spacing: 1px; }
  .brand__tagline { font-size: 13px; font-weight: 400; margin-top: 6px; letter-spacing: .5px; }

  .card--front .brand { left: 150px; top: 230px; color: var(--white); }
  .card--front .brand__name { font-size: 54px; }
  .card--front .brand__dot { background: var(--aqua); }

  .card--back .brand { right: 60px; top: 150px; align-items: flex-end; color: var(--teal); }
  .card--back .brand__name { font-size: 40px; }
  .card--back .brand__dot { background: var(--aqua); }

  .person { position: absolute; left: 60px; top: 330px; color: var(--teal); }
  .person__name { font-size: 30px; font-weight: 800; letter-spacing: 1px; }
  .person__role { font-size: 18px; font-weight: 600; color: var(--aqua); margin-top: 4px; }

  .contacts { position: absolute; left: 420px; top: 300px; list-style: none; color: var(--ink); font-size: 15px; }
  .contacts li { display: flex; align-items: center; gap: 12px; margin-bottom: 10px; }
  .contacts svg { width: 20px; height: 20px; flex: none; }

  .footer-bar { position: absolute; left: 0; right: 0; bottom: 0; height: 20px; background: var(--teal); }
  .footer-bar::before { content: ""; position: absolute; left: 60px; top: -8px; width: 160px; height: 8px; background: var(--aqua); }
</style>
</head>
<body>
  <section class="card card--front">
    <div class="pattern--front" role="img" aria-label="Padrão decorativo de folhas em traço branco"></div>
    <div class="brand">
      <div class="brand__row"><span class="brand__dot"></span><span class="brand__name">LAÇO SERENO</span></div>
      <span class="brand__tagline">assistência familiar e funerária</span>
    </div>
  </section>

  <section class="card card--back">
    <div class="pattern--back" role="img" aria-label="Padrão decorativo de folhas em cinza claro"></div>
    <div class="brand">
      <div class="brand__row"><span class="brand__dot"></span><span class="brand__name">LAÇO SERENO</span></div>
      <span class="brand__tagline">assistência familiar e funerária</span>
    </div>
    <div class="person">
      <p class="person__name">NOME COMPLETO</p>
      <p class="person__role">Cargo ou função</p>
    </div>
    <ul class="contacts">
      <li>
        <svg viewBox="0 0 24 24"><path fill="#1e8c82" d="M6.6 10.8a15 15 0 0 0 6.6 6.6l2.2-2.2c.3-.3.7-.4 1-.2 1.1.4 2.3.6 3.6.6.6 0 1 .4 1 1V20c0 .6-.4 1-1 1A17 17 0 0 1 3 4c0-.6.4-1 1-1h3.5c.6 0 1 .4 1 1 0 1.3.2 2.5.6 3.6.1.3 0 .7-.2 1z"/></svg>
        (00) 0000-0000 | (00) 00000-0000
      </li>
      <li>
        <svg viewBox="0 0 24 24"><rect x="2" y="5" width="20" height="14" rx="2" fill="none" stroke="#1e8c82" stroke-width="2"/><path d="M3 6l9 7 9-7" fill="none" stroke="#1e8c82" stroke-width="2"/></svg>
        contato@lacosereno.com.br
      </li>
      <li>
        <svg viewBox="0 0 24 24"><path fill="#1e8c82" d="M12 2a7 7 0 0 0-7 7c0 5 7 13 7 13s7-8 7-13a7 7 0 0 0-7-7zm0 9.5A2.5 2.5 0 1 1 12 6.5a2.5 2.5 0 0 1 0 5z"/></svg>
        Rua das Flores, 120 - Centro<br>Cidade - UF, 00000-000
      </li>
      <li>
        <svg viewBox="0 0 24 24"><circle cx="12" cy="12" r="9" fill="none" stroke="#1e8c82" stroke-width="2"/></svg>
        @lacosereno
      </li>
    </ul>
    <div class="footer-bar"></div>
  </section>
</body>
</html>
```